Progressive/contemporary business card design for successful Startups as a Service Company

New logo launched in 2020. New website launched in 2021. Now that COVID is (mostly) behind us, I'm networking with more people and need a business card that matches the company/logo design aesthetic.

```html
<!DOCTYPE html>
<html lang="en">
<head>
<meta charset="UTF-8">
<title>NorthPath Business Card</title>
<link rel="stylesheet" href="https://fonts.googleapis.com/css2?family=Montserrat:wght@300;400;500;700;800&display=swap">
<style>
  :root {
    --stage: #55595d;
    --ink-black: #000000;
    --paper: #ffffff;
    --slate: #3a4257;
    --muted-grey: #6b6f74;
    --name-blue: #1a5fa8;
    --magenta: #e4148c;
    --lime: #b4d22a;
    --green: #1fa148;
  }
  * { box-sizing: border-box; margin: 0; padding: 0; }
  html, body { width: 1200px; height: 780px; overflow: hidden; }
  body {
    background: var(--stage);
    font-family: "Montserrat", sans-serif;
    position: relative;
  }
  .card {
    position: absolute;
    top: 230px;
    width: 560px;
    height: 320px;
    border-radius: 22px;
    overflow: hidden;
    box-shadow: 0 10px 24px rgba(0,0,0,.35);
  }
  .card--back { left: 27px; background: var(--ink-black); }
  .card--front { left: 613px; background: var(--paper); }

  .wordmark {
    position: absolute;
    display: flex;
    align-items: center;
    gap: 14px;
    font-weight: 500;
    letter-spacing: .2em;
    line-height: 1;
  }
  .wordmark__square {
    display: block;
    background: var(--magenta);
  }
  .card--back .wordmark {
    left: 110px; top: 128px;
    font-size: 42px;
    color: var(--paper);
  }
  .card--back .wordmark__square { width: 34px; height: 34px; }
  .card--front .wordmark {
    right: 36px; top: 38px;
    font-size: 26px;
    color: var(--slate);
    gap: 10px;
  }
  .card--front .wordmark__square { width: 22px; height: 22px; }

  .web--back {
    position: absolute;
    right: 40px; bottom: 42px;
    font-size: 14px;
    font-weight: 700;
    color: var(--magenta);
  }

  .contact {
    position: absolute;
    left: 285px; top: 120px;
    list-style: none;
    color: var(--muted-grey);
    font-size: 13px;
    font-weight: 400;
    line-height: 1.3;
  }
  .contact__item {
    display: flex;
    align-items: center;
    gap: 10px;
    margin-bottom: 10px;
  }
  .contact__icon { flex: none; width: 20px; height: 20px; }

  .holder {
    position: absolute;
    left: 36px; top: 196px;
  }
  .holder__name {
    font-size: 23px;
    font-weight: 800;
    color: var(--name-blue);
  }
  .holder__role {
    font-size: 18px;
    font-weight: 300;
    color: var(--magenta);
    margin-top: 2px;
  }

  .band {
    position: absolute;
    left: 0; right: 0; bottom: 0;
    height: 56px;
    background: linear-gradient(90deg, var(--lime) 0%, var(--lime) 35%, var(--green) 100%);
  }
  .web--front {
    position: absolute;
    right: 36px; bottom: 19px;
    font-size: 14px;
    font-weight: 700;
    color: var(--paper);
  }
</style>
</head>
<body>

  <section class="card card--back" aria-label="Business card back">
    <div class="wordmark"><span>NORTHPATH</span><span class="wordmark__square"></span></div>
    <p class="web web--back">www.northpath.works</p>
  </section>

  <section class="card card--front" aria-label="Business card front">
    <div class="wordmark"><span>NORTHPATH</span><span class="wordmark__square"></span></div>

    <ul class="contact">
      <li class="contact__item">
        <svg class="contact__icon" viewBox="0 0 20 20" aria-hidden="true">
          <circle cx="10" cy="10" r="10" fill="var(--magenta)"/>
          <path d="M10 4.5a3.6 3.6 0 0 0-3.6 3.6c0 2.7 3.6 6.9 3.6 6.9s3.6-4.2 3.6-6.9A3.6 3.6 0 0 0 10 4.5z" fill="#fff"/>
          <circle cx="10" cy="8.1" r="1.4" fill="var(--magenta)"/>
        </svg>
        <span>1207 Larkfield Ave., Unit C<br>Brookvale, IL 60999</span>
      </li>
      <li class="contact__item">
        <svg class="contact__icon" viewBox="0 0 20 20" aria-hidden="true">
          <circle cx="10" cy="10" r="10" fill="var(--magenta)"/>
          <path d="M6.6 5.2l1.6-.4 1.1 2.6-1.2.9a6.4 6.4 0 0 0 3.4 3.4l.9-1.2 2.6 1.1-.4 1.6c-.2.6-.8 1-1.4.9A8.4 8.4 0 0 1 5.7 6.6c-.1-.6.3-1.2.9-1.4z" fill="#fff"/>
        </svg>
        <span>(555) 013-4872</span>
      </li>
      <li class="contact__item">
        <svg class="contact__icon" viewBox="0 0 20 20" aria-hidden="true">
          <circle cx="10" cy="10" r="10" fill="var(--magenta)"/>
          <rect x="5" y="6.5" width="10" height="7" rx="1" fill="#fff"/>
          <path d="M5.4 7l4.6 3.6L14.6 7" fill="none" stroke="var(--magenta)" stroke-width="1.1"/>
        </svg>
        <span>hello@northpathventures.com</span>
      </li>
    </ul>

    <div class="holder">
      <p class="holder__name">Dana Whitfield</p>
      <p class="holder__role">Owner</p>
    </div>

    <div class="band"></div>
    <p class="web web--front">www.northpath.works</p>
  </section>

</body>
</html>
```